Car Detailing product label for 750ML Clear Bottle

I need a label for various product with differente color for each products but in the same size bottle each time. It's only for our purpose no commercial application. I need a template with differente color but same design. The name for product it's : Tidal Quartz. We dont have any logo because it's only for us. We like like car silhouette in the logo or in background or something like that.

And for the product we have many like : APC Cleaner, Drying Aid, Wheel Cleaner and some other.

```html
<!DOCTYPE html>
<html lang="en">
<head>
<meta charset="utf-8">
<title>Tidal Quartz – Detailing Label Range</title>
<link rel="stylesheet" href="https://fonts.googleapis.com/css2?family=Russo+One&family=Roboto+Condensed:wght@400;700&display=swap">
<style>
  :root {
    --backdrop: #d2d2d2;
    --label-black: #141414;
    --label-edge: #262626;
    --title-white: #f4f4f4;
    --fine-grey: #8a8a8a;
    --accent-yellow: #e6e21c;
    --accent-red: #d3201f;
    --accent-green: #2fbf2a;
    --accent-blue: #2546d8;
  }
  * { box-sizing: border-box; margin: 0; padding: 0; }
  html, body { width: 835px; height: 1200px; overflow: hidden; }
  body {
    background: var(--backdrop);
    font-family: "Roboto Condensed", sans-serif;
    position: relative;
  }
  .label-row {
    position: absolute;
    left: 0;
    width: 835px;
    display: flex;
    justify-content: center;
    gap: 35px;
  }
  .label-row--top { top: 150px; }
  .label-row--bottom { top: 740px; }

  .label {
    --accent: var(--accent-yellow);
    position: relative;
    width: 160px;
    height: 380px;
    background: var(--label-black);
    border: 1px solid var(--label-edge);
    border-radius: 4px;
    overflow: hidden;
  }
  .label--red { --accent: var(--accent-red); }
  .label--green { --accent: var(--accent-green); }
  .label--blue { --accent: var(--accent-blue); }

  .tread-band {
    position: absolute;
    left: -40px;
    top: 120px;
    width: 240px;
    height: 120px;
    transform: rotate(-28deg);
    background: linear-gradient(90deg, transparent 0%, var(--accent) 18%, var(--accent) 82%, transparent 100%);
    opacity: 0.9;
  }
  .side-note {
    position: absolute;
    left: 6px;
    top: 40px;
    writing-mode: vertical-rl;
    transform: rotate(180deg);
    font-size: 7px;
    letter-spacing: 0.5px;
    color: var(--fine-grey);
  }
  .brand-name {
    position: absolute;
    left: 14px;
    top: 150px;
    font-family: "Russo One", sans-serif;
    font-size: 31px;
    font-weight: 400;
    line-height: 0.95;
    color: var(--title-white);
    text-transform: uppercase;
  }
  .product-name {
    position: absolute;
    left: 14px;
    top: 232px;
    padding: 2px 6px;
    font-size: 13px;
    font-weight: 700;
    line-height: 1.2;
    color: var(--title-white);
    background: var(--label-black);
  }
  .directions {
    position: absolute;
    left: 16px;
    right: 12px;
    bottom: 22px;
    font-size: 7px;
    line-height: 1.4;
    color: var(--fine-grey);
  }
</style>
</head>
<body>
  <section class="label-row label-row--top">
    <article class="label">
      <div class="tread-band" role="img" aria-label="Tire tread splatter in accent colour"></div>
      <p class="side-note">Safe on all surfaces</p>
      <h2 class="brand-name">Tidal<br>Quartz</h2>
      <p class="product-name">APC Cleaner</p>
      <p class="directions">Spray, wipe, rinse clean.</p>
    </article>
    <article class="label">
      <div class="tread-band" role="img" aria-label="Tire tread splatter in accent colour"></div>
      <p class="side-note">Safe on all surfaces</p>
      <h2 class="brand-name">Tidal<br>Quartz</h2>
      <p class="product-name">APC Cleaner</p>
      <p class="directions">Spray, wipe, rinse clean.</p>
    </article>
    <article class="label">
      <div class="tread-band" role="img" aria-label="Tire tread splatter in accent colour"></div>
      <p class="side-note">Safe on all surfaces</p>
      <h2 class="brand-name">Tidal<br>Quartz</h2>
      <p class="product-name">APC Cleaner</p>
      <p class="directions">Spray, wipe, rinse clean.</p>
    </article>
  </section>

  <section class="label-row label-row--bottom">
    <article class="label label--red">
      <div class="tread-band" role="img" aria-label="Tire tread splatter in red"></div>
      <p class="side-note">Safe on all surfaces</p>
      <h2 class="brand-name">Tidal<br>Quartz</h2>
      <p class="product-name">APC Cleaner</p>
      <p class="directions">Spray, wipe, rinse clean.</p>
    </article>
    <article class="label">
      <div class="tread-band" role="img" aria-label="Tire tread splatter in yellow"></div>
      <p class="side-note">Safe on all surfaces</p>
      <h2 class="brand-name">Tidal<br>Quartz</h2>
      <p class="product-name">APC Cleaner</p>
      <p class="directions">Spray, wipe, rinse clean.</p>
    </article>
    <article class="label label--green">
      <div class="tread-band" role="img" aria-label="Tire tread splatter in green"></div>
      <p class="side-note">Safe on all surfaces</p>
      <h2 class="brand-name">Tidal<br>Quartz</h2>
      <p class="product-name">APC Cleaner</p>
      <p class="directions">Spray, wipe, rinse clean.</p>
    </article>
    <article class="label label--blue">
      <div class="tread-band" role="img" aria-label="Tire tread splatter in blue"></div>
      <p class="side-note">Safe on all surfaces</p>
      <h2 class="brand-name">Tidal<br>Quartz</h2>
      <p class="product-name">APC Cleaner</p>
      <p class="directions">Spray, wipe, rinse clean.</p>
    </article>
  </section>
</body>
</html>
```